Picket Sign Advertising For Alaska Tour Company

I would like a relator style picket sign made that I can place by the water near hotels to generate phone calls and website visits. I want to Advertise Our Daily Jet Boat Tours & Jet Ski Tours. This will be a one sided sign. You may be able to see our past brochure and flyer designs and logo. Our FB page is Harlow Summit Excursions and our website is harlowsummitexcursions.com or contact number is 907-418-5563

```html
<!DOCTYPE html>
<html lang="en">
<head>
<meta charset="utf-8">
<title>Harlow Summit Excursions – Jet Ski &amp; Jet Boat Tours Sign</title>
<link rel="stylesheet" href="https://fonts.googleapis.com/css2?family=Anton&family=Oswald:wght@500;700&family=Montserrat:wght@600;800&display=swap">
<style>
  :root {
    --page: #ecebe7;
    --black: #000000;
    --yellow: #ffdf1a;
    --banner-yellow: #fce011;
    --red: #e3191f;
    --teal: #1f8aa6;
    --ring: #eef4f7;
    --gold: #b39a6a;
    --cream: #f4ecc4;
    --white: #ffffff;
    --badge: #3b3b3b;
  }
  * { margin: 0; padding: 0; box-sizing: border-box; }
  html, body { width: 1200px; height: 900px; overflow: hidden; }
  body { background: var(--page); position: relative; font-family: "Oswald", sans-serif; }

  .sign {
    position: absolute; left: 333px; top: 20px;
    width: 534px; height: 860px;
    background: var(--black);
    overflow: hidden;
    box-shadow: 3px 4px 8px rgba(0,0,0,0.35);
  }
  .sign__photo {
    position: absolute; left: 0; top: 0; width: 100%; height: 440px;
    background: linear-gradient(180deg,
      #c9ccd6 0%, #9fb0c0 6%, #3f6a33 14%, #2f5a28 30%,
      #6f8f3a 38%, #8fa04e 45%, #6c6a60 52%, #7a7870 70%,
      #55544f 84%, #000 100%);
  }

  .banner {
    position: absolute; left: 8px; top: 368px;
    width: 506px; height: 184px;
    transform: rotate(-13deg);
    background: var(--banner-yellow);
    border: 11px solid var(--red);
    border-radius: 30px;
    display: flex; flex-direction: column; justify-content: center;
    padding-left: 24px;
    z-index: 3;
  }
  .banner__line {
    font-family: "Anton", sans-serif;
    color: var(--black);
    font-size: 78px; line-height: 0.98;
    white-space: nowrap;
  }

  .book-now {
    position: absolute; left: 354px; top: 476px;
    width: 160px; height: 160px; border-radius: 50%;
    background: var(--ring);
    box-shadow: inset 0 -6px 10px rgba(0,0,0,0.25);
    z-index: 2;
  }
  .book-now__face {
    position: absolute; inset: 10px; border-radius: 50%;
    background: radial-gradient(circle at 50% 35%, #3aa5bf 0%, var(--teal) 70%);
    display: flex; flex-direction: column; align-items: center; justify-content: center;
    transform: rotate(-13deg);
    padding-top: 24px;
  }
  .book-now__text {
    font-family: "Anton", sans-serif; color: var(--red);
    font-size: 42px; line-height: 1;
  }

  .phone {
    position: absolute; left: 0; width: 100%; top: 640px;
    text-align: center;
    font-family: "Oswald", sans-serif; font-weight: 700;
    color: var(--yellow); font-size: 56px; line-height: 1;
    padding-right: 30px;
  }

  .brand {
    position: absolute; left: 18px; top: 703px;
    display: flex; align-items: center; gap: 14px;
  }
  .brand__mark { width: 86px; height: 86px; border-radius: 50%; background: var(--gold); }
  .brand__name {
    font-family: "Oswald", sans-serif; font-weight: 500; color: var(--gold);
    text-transform: uppercase; line-height: 1.05;
  }
  .brand__name-main { display: block; font-size: 33px; letter-spacing: 1px; }
  .brand__name-sub { display: block; font-size: 16px; letter-spacing: 9px; }

  .tagline {
    position: absolute; left: 18px; top: 792px;
    font-family: "Montserrat", sans-serif; font-weight: 600;
    color: var(--white); font-size: 10px; letter-spacing: 4.6px;
    white-space: nowrap;
  }

  .listing { position: absolute; left: 428px; width: 90px; height: 34px; border-radius: 17px; background: var(--badge); }
  .listing--first { top: 710px; }
  .listing--second { top: 772px; }

  .web-band {
    position: absolute; left: 0; bottom: 0; width: 100%; height: 43px;
    background: var(--cream);
    display: flex; align-items: center; justify-content: center;
  }
  .web-band__url {
    font-family: "Montserrat", sans-serif; font-weight: 800;
    font-size: 15px; letter-spacing: 7px; color: var(--black);
  }
</style>
</head>
<body>
  <main class="sign">
    <div class="sign__photo" role="img" aria-label="Photo of a jet ski and a green jet boat on an Alaskan river with two guides standing on the boat, trees and a large outdoor letter sign on the grassy bank behind"></div>

    <div class="banner">
      <span class="banner__line">Jet Ski Tours</span>
      <span class="banner__line">Jet Boat Tours</span>
    </div>

    <div class="book-now">
      <div class="book-now__face">
        <span class="book-now__text">BOOK</span>
        <span class="book-now__text">Now</span>
      </div>
    </div>

    <p class="phone">907-418-5563</p>

    <div class="brand">
      <span class="brand__mark"></span>
      <p class="brand__name">
        <span class="brand__name-main">Harlow Summit</span>
        <span class="brand__name-sub">Excursions</span>
      </p>
    </div>

    <p class="tagline">RIDE THE RIVERS OF THE NORTHLAND</p>

    <span class="listing listing--first" role="img" aria-label="Travel review listing badge"></span>
    <span class="listing listing--second" role="img" aria-label="Lodging listing badge"></span>

    <div class="web-band">
      <span class="web-band__url">harlowsummitexcursions.com</span>
    </div>
  </main>
</body>
</html>
```